Innovative healthcare collaborative needs new look for business cards

CareLoomQ is a new kind of healthcare relationship company focused on aligning partners, innovation and solutions to provide needed health services to healthcare systems, hospitals or private business. Not mired in the old merger and acquisition fee-for-service framework, we focus on primary, secondary and tertiary service area partnership collaboratives. These networks are constructed by aligning healthcare services along a network of care, not just an individual patient care plan. This involves partnership arrangements with large or small medical centers, physician groups, allied health services, public health agencies, health insurers, et al as well as civic agencies, schools, farmers, supply chains to bring about needed healthcare solutions for patients. Think Green Havens. GH does for communities what we do for hospitals and health systems. We educate and instruct on strategic, operational, and innovative solutions for a healthcare provider, practice, business, or system resulting in successful construction of care networks (legal entity). We provide the blueprint of how to do this type of partnership, focused on what’s best for the sustainability of the business and the people (patients or potential patients) living there. Rural hospitals in particular are at risk.
We also provide seminars to academic, medical academic, and private industry to instruct on how to construct these care networks and educate on the essential criteria to be successful in the new healthcare era. We have been doing this work for the past 8 years, and since COVID-19, the recognition of fractured processes has boosted the demand. We need a business card that sets the tone that the traditional healthcare delivery system in the US has transformed (overnight). Our company is educating on how to transition current business models to the new world order in this space.
Brainstormed some business card tag lines for consideration:
CareLoomQ
• a healthcaring company
• allbettertogether
• connecting for the greater good

Target Market(s)

Health systems, hospitals, physician practices, academic medical schools, residency programs

Industry/Entity Type

Healthcare

Contact Information for Business Card

Doreen Vashtoll, Chief Relationship Officer
doreenvashtoll@mailpost-example.net
mobile: 415-286-9043

Font styles to use
Serif
Sans Serif

Requirements
Should not have
• Do not use word Consultant

```html
<!DOCTYPE html>
<html lang="en">
<head>
<meta charset="UTF-8">
<title>CareLoomQ Business Card</title>
<link href="https://fonts.googleapis.com/css2?family=Montserrat:wght@800&family=Jost:wght@300;400&display=swap" rel="stylesheet">
<style>
  :root {
    --bg: #e9eeee;
    --card: #ffffff;
    --brand-blue: #0f6fbf;
    --brand-faint: #b6d5ea;
    --text-grey: #6a6a6a;
    --edge: #d4d8d8;
  }
  * { margin: 0; padding: 0; box-sizing: border-box; }
  html, body {
    width: 1200px; height: 900px; overflow: hidden;
    background: var(--bg);
  }
  .sheet {
    width: 1200px; height: 900px;
    display: flex; align-items: center; justify-content: center; gap: 40px;
  }
  .card {
    position: relative;
    width: 560px; height: 320px;
    background: var(--card);
    box-shadow: 0 2px 0 var(--edge), 0 10px 24px rgba(0,0,0,0.08);
    overflow: hidden;
  }
  /* Back: contact side */
  .contact-block { position: absolute; left: 44px; top: 70px; }
  .person-name {
    font-family: "Montserrat", sans-serif; font-weight: 800;
    font-size: 30px; color: var(--brand-blue); line-height: 1.1;
  }
  .person-title {
    font-family: "Jost", sans-serif; font-weight: 300;
    font-size: 27px; color: var(--text-grey); line-height: 1.2;
  }
  .contact-list { list-style: none; margin-top: 26px; }
  .contact-list li {
    display: flex; align-items: center; gap: 12px;
    font-family: "Jost", sans-serif; font-weight: 300;
    font-size: 16px; color: var(--text-grey); letter-spacing: 0.5px;
    margin-bottom: 6px;
  }
  .contact-icon { width: 14px; height: 14px; fill: var(--brand-blue); flex: none; }
  .wordmark-faint {
    position: absolute; right: -18px; bottom: -14px;
    font-family: "Montserrat", sans-serif; font-weight: 800;
    font-size: 96px; color: var(--brand-faint); letter-spacing: -2px;
    white-space: nowrap;
  }
  /* Front: wordmark side */
  .card-front { display: flex; align-items: center; justify-content: center; }
  .wordmark {
    font-family: "Montserrat", sans-serif; font-weight: 800;
    font-size: 58px; color: var(--brand-blue); letter-spacing: -1px;
  }
</style>
</head>
<body>
<main class="sheet">
  <section class="card card-back">
    <div class="contact-block">
      <h1 class="person-name">Doreen Vashtoll</h1>
      <p class="person-title">Chief Relationship Officer</p>
      <ul class="contact-list">
        <li>
          <svg class="contact-icon" viewBox="0 0 16 16" aria-hidden="true"><path d="M3 1l3 3-2 2c1 2 3 4 5 5l2-2 3 3-2 3C6 14 2 10 1 3z"/></svg>
          415-286-9043
        </li>
        <li>
          <svg class="contact-icon" viewBox="0 0 16 16" aria-hidden="true"><path d="M1 3h14v10H1z M1 3l7 6 7-6" stroke="#fff" stroke-width="1"/></svg>
          doreenvashtoll@mailpost-example.net
        </li>
        <li>
          <svg class="contact-icon" viewBox="0 0 16 16" aria-hidden="true"><circle cx="8" cy="8" r="7"/><path d="M1 8h14M8 1c-3 4-3 10 0 14M8 1c3 4 3 10 0 14" stroke="#fff" fill="none" stroke-width="1"/></svg>
          www.careloomq-example.net
        </li>
      </ul>
    </div>
    <div class="wordmark-faint" aria-hidden="true">CareLoomQ</div>
  </section>

  <section class="card card-front">
    <div class="wordmark">CareLoomQ</div>
  </section>
</main>
</body>
</html>
```